Change the world and help build JumpKOV.tv!

We need a mobile website design for our Beta release - see wireframes attached.
See our Logo design files attached along with fonts, etc.
Please see enclosed .PDF that provides a great overview of our company, KOV.
Any questions, feel free to ask - we're very engaged here on Pixel Harbor and will make ourselves available.
Thanks!
Tomas
Updates
Very pleased with what's coming in! Would like to see some more variety and more volume of designs.
Target Market(s)
Ages 13+ (all genders, races, creeds, income levels, etc)
Coding
Coded - Design and coding required
Number of Pages Required
5+ page
Font styles to use
Colors
Designer to choose colors to be used in the design.
Look and feel
Each slider illustrates characteristics of the customer's brand and the style your logo design should communicate.

```html
<!DOCTYPE html>
<html lang="en">
<head>
<meta charset="UTF-8">
<title>KOV Beta Sign-up</title>
<link rel="stylesheet" href="https://fonts.googleapis.com/css2?family=Lato:wght@400;700&display=swap">
<style>
  :root {
    --navy: #1c2a52;
    --navy-light: #2f5584;
    --text-grey: #8c8c8c;
    --field-border: #c9c9c9;
    --footer-text: #2b2b2b;
    --white: #ffffff;
  }
  * { margin: 0; padding: 0; box-sizing: border-box; }
  html, body {
    width: 1200px;
    height: 3107px;
    overflow: hidden;
    background: var(--white);
    font-family: "Lato", sans-serif;
  }
  .page {
    position: relative;
    width: 1200px;
    height: 3107px;
  }
  .top-bar {
    position: absolute;
    left: 0; top: 0;
    width: 1200px; height: 141px;
    background: var(--navy);
  }
  .intro {
    position: absolute;
    left: 45px; top: 208px;
    width: 1130px;
    font-size: 54px;
    line-height: 96px;
    color: var(--text-grey);
    font-weight: 400;
  }
  .field-label {
    position: absolute;
    left: 42px;
    font-size: 54px;
    line-height: 64px;
    color: var(--text-grey);
  }
  .field-input {
    position: absolute;
    left: 45px;
    width: 1101px;
    height: 115px;
    border: 3px solid var(--field-border);
    border-radius: 13px;
    background: var(--white);
  }
  .field-input--story { height: 208px; }
  .register-button {
    position: absolute;
    left: 765px; top: 2704px;
    width: 381px; height: 144px;
    border: none;
    border-radius: 16px;
    background: linear-gradient(160deg, var(--navy-light) 0%, var(--navy) 45%, var(--navy) 100%);
    color: var(--white);
    font-family: "Lato", sans-serif;
    font-size: 43px;
    letter-spacing: 1px;
    display: flex;
    align-items: center;
    justify-content: center;
  }
  .footer-links {
    position: absolute;
    left: 0; top: 2922px;
    width: 1200px;
    height: 40px;
  }
  .footer-link {
    position: absolute;
    top: 0;
    font-size: 30px;
    line-height: 40px;
    color: var(--footer-text);
    text-decoration: none;
    white-space: nowrap;
  }
  .bottom-bar {
    position: absolute;
    left: 0; top: 2998px;
    width: 1200px; height: 109px;
    background: var(--navy);
  }
</style>
</head>
<body>
<div class="page">
  <header class="top-bar"></header>

  <p class="intro">Sign-up to receive an invitation to join our<br>pre-launch (Beta) version of KOV! Join<br>our growing community of mental health<br>warriors and help build a platform that<br>can improve the lives of millions of<br>people.</p>

  <form class="signup-form">
    <label class="field-label" style="top:874px">Name</label>
    <div class="field-input" style="top:950px"></div>

    <label class="field-label" style="top:1162px">Date of birth</label>
    <div class="field-input" style="top:1248px"></div>

    <label class="field-label" style="top:1450px">Address</label>
    <div class="field-input" style="top:1533px"></div>

    <label class="field-label" style="top:1738px">Email</label>
    <div class="field-input" style="top:1830px"></div>

    <label class="field-label" style="top:2026px">Phone</label>
    <div class="field-input" style="top:2122px"></div>

    <label class="field-label" style="top:2314px">Share your story with us</label>
    <div class="field-input field-input--story" style="top:2403px"></div>

    <div class="register-button">REGISTER</div>
  </form>

  <nav class="footer-links">
    <a class="footer-link" style="left:45px">Terms and Condition</a>
    <a class="footer-link" style="left:426px">Privacy Policy</a>
    <a class="footer-link" style="left:701px">About KOV</a>
    <a class="footer-link" style="left:934px">The KOV Team</a>
  </nav>

  <footer class="bottom-bar"></footer>
</div>
</body>
</html>
```